Business Card Design Project

Business and Appointment Card for Medical Practice. On back of card we would like to have: blank line for patient name, Mon-Fri each with a check box next to the day, blank line for appointment date, blank line for appointment time, with option to circle am or pm.

Target Market(s)

Professional Business Associates, as well as function as patient appointment cards (on back side of card)

Industry/Entity Type

Business

Colors

Designer to choose colors to be used in the design.

```html
<!DOCTYPE html>
<html lang="en">
<head>
<meta charset="utf-8">
<title>Maple Grove Medical Associates – Business &amp; Appointment Card</title>
<link href="https://fonts.googleapis.com/css2?family=Questrial&family=Tinos&display=swap" rel="stylesheet">
<style>
  :root{
    --bg:#ece8e3;
    --card:#ffffff;
    --green:#0b6a22;
    --green-dark:#064f18;
    --red:#8b1a1f;
    --grey:#7d8083;
    --blossom:#f1dfe1;
    --ink:#3a3a3a;
  }
  *{box-sizing:border-box;margin:0;padding:0}
  html,body{width:1200px;height:900px;overflow:hidden;background:var(--bg)}
  .canvas{position:relative;width:1200px;height:900px}
  .card{position:absolute;left:250px;width:700px;height:400px;overflow:hidden;
        box-shadow:0 6px 18px rgba(0,0,0,.18)}
  .card--front{top:30px;background:var(--card)}
  .card--back{top:470px;background:var(--green)}

  /* front */
  .brand{position:absolute;left:36px;top:140px;width:370px;display:flex;align-items:center;justify-content:center;gap:12px}
  .brand__mark{width:14px;height:14px;background:var(--green);flex:none}
  .brand__name{font-family:'Questrial',sans-serif;color:var(--red);font-size:26px;line-height:1.2}
  .divider{position:absolute;left:430px;top:30px;width:2px;height:240px;
           background:linear-gradient(var(--grey),#c9cacb)}
  .contact{position:absolute;left:447px;top:30px;font-family:'Questrial',sans-serif;color:var(--grey);font-size:20px;line-height:1.25}
  .contact__name{color:var(--red);font-size:24px}
  .contact__role{font-size:24px;margin-bottom:24px}
  .contact__address{margin-bottom:24px}
  .contact__label{color:var(--red)}
  .footer-bands{position:absolute;left:0;top:300px;width:700px;height:100px}
  .website{position:absolute;left:40px;top:314px;font-family:'Questrial',sans-serif;color:#fff;font-size:23px;letter-spacing:.5px}

  /* back */
  .dome{position:absolute;left:0;top:0}
  .blossom-tree{position:absolute;left:330px;top:90px;width:220px;height:200px;border-radius:50%;
                background:radial-gradient(circle,var(--blossom) 0%,rgba(241,223,225,.35) 60%,rgba(255,255,255,0) 75%)}
  .appointment{position:absolute;left:150px;top:40px;width:500px;font-family:'Tinos',serif;color:var(--ink);font-size:17px}
  .appointment__title{color:var(--red);font-size:24px;letter-spacing:2px;text-align:center;margin-bottom:14px}
  .field{display:flex;align-items:flex-end;gap:8px;margin-bottom:14px}
  .field__line{flex:1;border-bottom:1px solid var(--ink);height:18px}
  .days{display:flex;justify-content:space-between;margin:8px 0 18px}
  .day{display:flex;flex-direction:column;align-items:center;gap:6px}
  .day__box{width:34px;height:30px;border:2px solid var(--red);border-radius:50%}
  .ampm{white-space:nowrap}
</style>
</head>
<body>
<div class="canvas">

  <section class="card card--front" aria-label="Business card front">
    <div class="brand">
      <span class="brand__mark"></span>
      <p class="brand__name">Maple Grove Medical Associates</p>
    </div>
    <div class="divider"></div>
    <div class="contact">
      <p class="contact__name">Your Name</p>
      <p class="contact__role">President</p>
      <p class="contact__address">48 Linden Ave. 5th Floor<br>Easton, MA 02375</p>
      <p><span class="contact__label">Phone:</span> 555-010-2040</p>
      <p><span class="contact__label">Mobile:</span> 555-010-7731</p>
      <p><span class="contact__label">Email:</span> hello@maplegrovemed.com</p>
    </div>
    <svg class="footer-bands" viewBox="0 0 700 100" width="700" height="100">
      <polygon points="0,10 700,10 700,38 520,38 505,50 0,50" fill="var(--green)"/>
      <polygon points="0,56 510,56 525,44 700,44 700,78 0,78" fill="var(--red)"/>
    </svg>
    <p class="website">www.maplegrovemed.com</p>
  </section>

  <section class="card card--back" aria-label="Appointment card back">
    <svg class="dome" viewBox="0 0 700 400" width="700" height="400">
      <circle cx="400" cy="330" r="395" fill="var(--green-dark)"/>
      <circle cx="400" cy="330" r="378" fill="#fff"/>
    </svg>
    <div class="blossom-tree" role="img" aria-label="Faint blossoming tree decoration"></div>
    <div class="appointment">
      <p class="appointment__title">APPOINTMENT</p>
      <div class="field"><span>Patient Name:</span><span class="field__line"></span></div>
      <div class="field"><span>Reason For Appointment:</span><span class="field__line"></span></div>
      <div class="days">
        <div class="day"><span class="day__box"></span>Mon</div>
        <div class="day"><span class="day__box"></span>Tue</div>
        <div class="day"><span class="day__box"></span>Wed</div>
        <div class="day"><span class="day__box"></span>Thu</div>
        <div class="day"><span class="day__box"></span>Fri</div>
      </div>
      <div class="field"><span>Date:</span><span class="field__line"></span></div>
      <div class="field"><span>Time:</span><span class="field__line"></span><span class="ampm">am / pm</span></div>
    </div>
  </section>

</div>
</body>
</html>
```